UPDATE 2: I HAVE ATTACHED TWO PHOTOS; PLEASE CONSIDER USING EITHER ONE IN A NEW DESIGN. THANK YOU.
UPDATE: I HAVE INCLUDED 4 SAMPLE BOOK COVERS THAT I LIKE TO HELP YOU ORIENT YOUR DESIGN WORK
Looking for book cover, spine, and back for a MEMOIR. Details:
TITLE: Winter's Bright Orchard
AUTHOR: Lorvina Pettigrue
GENRE: Memoir
STYLE REQUESTED: Abstract and colorful; designers are welcome to get creative. Note that the memoir takes place largely in a poor African American city.
BOOK SUMMARY: As a young girl, Lorvina Pettigrue—or “Lori” to her friends and family—discovers the man she thought was her father wasn’t, and her real biological father wants little if anything to do with her. What follows is the story of a girl’s longing, a longing disturbed by abuse, disappointment, and loneliness.
Set against the backdrop of Gary, Indiana—the then “murder capital of the world”—Winter’s Bright Orchard follows Lorvina as she searches and grows, following a path that eventually leads her to self-discovery and self-confidence.
Template provided for InDesign. Please note margins and bleed areas. Make sure any letters/words are at least one inch from edges. On spine, leave three inches at bottom for publisher's logo.
To all designers: Please note that there should NOT be any images of people as part of your designs. Thank you, and my apologies for not mentioning that in the initial ask.

```html
<!DOCTYPE html>
<html lang="en">
<head>
<meta charset="UTF-8">
<title>Winter's Bright Orchard — Book Cover</title>
<link href="https://fonts.googleapis.com/css2?family=Josefin+Sans:wght@400;600&display=swap" rel="stylesheet">
<style>
  :root {
    --page-bg: #ffffff;
    --sky-blue: #3a86a6;
    --sky-teal: #6b9aa8;
    --sky-haze: #a9aa98;
    --sky-gold: #c9a660;
    --horizon-ochre: #b8913c;
    --ridge-peach: #c08062;
    --ridge-rose: #b06a64;
    --ridge-mauve: #945a6e;
    --ridge-plum: #7c4766;
    --ridge-deep: #6a3c58;
    --city-gold: #d6a842;
    --city-ochre: #b88a34;
    --city-shadow: #4a3518;
    --ground-brown: #3b2a11;
    --title-white: #ffffff;
    --author-cream: #ebe3d3;
  }
  * { margin: 0; padding: 0; box-sizing: border-box; }
  html, body {
    width: 1200px; height: 1200px; overflow: hidden;
    background: var(--page-bg);
  }
  .cover {
    position: absolute; left: 220px; top: 30px;
    width: 760px; height: 1140px;
    background: var(--ground-brown);
    overflow: hidden;
    font-family: "Josefin Sans", sans-serif;
  }
  .sky {
    position: absolute; left: 0; top: 0; width: 760px; height: 440px;
    background:
      radial-gradient(ellipse 420px 40px at 30% 60px, rgba(220,230,235,0.35), transparent 70%),
      radial-gradient(ellipse 380px 30px at 70% 150px, rgba(225,225,215,0.30), transparent 70%),
      linear-gradient(to bottom,
        var(--sky-blue) 0%,
        var(--sky-teal) 14%,
        var(--sky-haze) 30%,
        var(--sky-gold) 52%,
        var(--horizon-ochre) 85%,
        var(--ridge-peach) 100%);
  }
  .mountains {
    position: absolute; left: 0; top: 440px; width: 760px; height: 300px;
    background:
      radial-gradient(ellipse 260px 120px at 0% 100%, rgba(70,40,45,0.7), transparent 70%),
      radial-gradient(ellipse 520px 90px at 65% 62%, rgba(106,60,88,0.55), transparent 72%),
      radial-gradient(ellipse 600px 80px at 40% 30%, rgba(176,106,100,0.5), transparent 72%),
      linear-gradient(to bottom,
        var(--ridge-peach) 0%,
        var(--ridge-rose) 22%,
        #a46070 40%,
        var(--ridge-mauve) 55%,
        var(--ridge-plum) 78%,
        var(--ridge-deep) 100%);
  }
  .cityscape {
    position: absolute; left: 0; top: 740px; width: 760px; height: 200px;
    background:
      radial-gradient(ellipse 110px 90px at 62% 45%, rgba(59,42,17,0.75), transparent 75%),
      radial-gradient(ellipse 90px 90px at 40% 55%, rgba(59,42,17,0.65), transparent 75%),
      radial-gradient(ellipse 90px 70px at 5% 60%, rgba(59,42,17,0.7), transparent 75%),
      radial-gradient(ellipse 80px 60px at 90% 60%, rgba(59,42,17,0.6), transparent 75%),
      linear-gradient(to bottom,
        var(--ridge-deep) 0%,
        var(--city-gold) 14%,
        var(--city-gold) 40%,
        var(--city-ochre) 62%,
        var(--city-shadow) 88%,
        var(--ground-brown) 100%);
  }
  .title {
    position: absolute; left: 0; right: 0; top: 165px;
    text-align: center;
    color: var(--title-white);
    font-weight: 600;
    font-size: 78px;
    line-height: 94px;
    letter-spacing: 0.26em;
    text-indent: 0.26em;
    text-transform: uppercase;
  }
  .title span { display: block; }
  .author {
    position: absolute; left: 0; right: 0; top: 955px;
    text-align: center;
    color: var(--author-cream);
    font-weight: 400;
    font-size: 50px;
    line-height: 58px;
    letter-spacing: 0.34em;
    text-indent: 0.34em;
    text-transform: uppercase;
  }
  .author span { display: block; }
</style>
</head>
<body>
  <main class="cover">
    <div class="sky" role="img" aria-label="Photograph of a sunset sky with wispy clouds fading from blue to gold"></div>
    <div class="mountains" role="img" aria-label="Photograph of layered hazy mountain ridges in rose, mauve and plum"></div>
    <div class="cityscape" role="img" aria-label="Illustrated silhouette of a dense city of low buildings and power lines in gold and dark brown"></div>
    <h1 class="title">
      <span>Winter's</span>
      <span>Bright</span>
      <span>Orchard</span>
    </h1>
    <p class="author">
      <span>Lorvina</span>
      <span>Pettigrue</span>
    </p>
  </main>
</body>
</html>
```